Book Cover for Senior Care Agencies

Design a cover [kindle and print] for a book of interviews with home health care agencies, that also has client stories [like a Lantern Tales of Kindness type book]

The title is
Hands That Stay

subtitle
Selecting A Trusted Elder Support Service

The book will have 7 co-authors, so they will need to be listed on the cover
Print book Size 6 x 9

For image, I like the idea of an adult helping their senior parent out... What i am going for is very, clean and crisp yet warm. No cartoons.

I don't tend to like script fonts.
thank you

Target Market(s)

Family members who have senior relatives or parents

Industry/Entity Type

Health Care

Font styles to use
Serif
Sans Serif

Requirements
Should not have
• cartoons

```html
<!DOCTYPE html>
<html lang="en">
<head>
<meta charset="utf-8">
<title>Hands That Stay – Cover Spread</title>
<link rel="stylesheet" href="https://fonts.googleapis.com/css2?family=Cinzel:wght@400&family=Lato:wght@400&family=Montserrat:wght@300&display=swap">
<style>
  :root {
    --canvas: #ffffff;
    --back-panel: #e0e7ea;
    --trim-line: #b9bcbe;
    --title-front: #93a6ae;
    --title-back: #5d5d5d;
    --ink: #222222;
    --body-ink: #2b2b2b;
    --photo-front-a: #5f5650;
    --photo-front-b: #d9cfc3;
    --photo-front-c: #f3f2f4;
    --photo-back-a: #c9dbe6;
    --photo-back-b: #7f86c9;
    --photo-back-c: #eef3f6;
  }
  * { box-sizing: border-box; margin: 0; padding: 0; }
  html, body { width: 1200px; height: 1000px; overflow: hidden; background: var(--canvas); }
  .canvas { position: relative; width: 1200px; height: 1000px; background: var(--canvas); }

  .page-number {
    position: absolute; left: 27px; top: 26px;
    font: 400 18px/1 "Lato", sans-serif; color: var(--ink);
  }

  .trim-line { position: absolute; top: 97px; width: 1px; height: 806px; background: var(--trim-line); }
  .trim-line--left { left: 571px; }
  .trim-line--right { left: 629px; }

  /* Back cover */
  .back-cover {
    position: absolute; left: 56px; top: 114px; width: 515px; height: 773px;
    background: var(--back-panel); border: 1px solid var(--trim-line); border-right: none;
  }
  .back-title {
    position: absolute; right: 250px; top: 40px; text-align: right;
    font: 300 50px/48px "Montserrat", sans-serif; color: var(--title-back); letter-spacing: -1px;
  }
  .back-title__line { display: block; }
  .back-subtitle {
    position: absolute; right: 400px; top: 100px; text-align: right;
    font: 400 10px/13px "Cinzel", serif; color: var(--ink);
  }
  .back-copy {
    position: absolute; left: 75px; top: 217px; width: 191px;
    font: 400 13.3px/23px "Lato", sans-serif; color: var(--body-ink);
    text-align: justify;
  }
  .back-copy p + p { margin-top: 23px; }
  .back-photo {
    position: absolute; left: 293px; top: 223px; width: 222px; height: 145px;
    background: linear-gradient(100deg, var(--photo-back-c) 0%, var(--photo-back-a) 35%, var(--photo-back-b) 48%, var(--photo-back-c) 62%, var(--photo-back-a) 100%);
  }

  /* Spine */
  .spine {
    position: absolute; left: 572px; top: 114px; width: 57px; height: 773px;
    display: flex; justify-content: center; align-items: flex-start; padding-top: 26px;
  }
  .spine-text {
    writing-mode: vertical-rl; white-space: nowrap; color: var(--ink);
    display: flex; align-items: center; gap: 14px;
  }
  .spine-title { font: 300 23px/1 "Montserrat", sans-serif; letter-spacing: 1px; color: #3a3a3a; }
  .spine-subtitle { font: 400 14.5px/1 "Cinzel", serif; letter-spacing: 0.5px; }

  /* Front cover */
  .front-cover {
    position: absolute; left: 629px; top: 114px; width: 516px; height: 773px;
    background: var(--canvas); border: 1px solid var(--trim-line); border-left: none;
  }
  .front-title {
    position: absolute; left: 66px; top: 48px;
    font: 300 98px/100px "Montserrat", sans-serif; color: var(--title-front); letter-spacing: -2px;
  }
  .front-title__line { display: block; }
  .front-subtitle {
    position: absolute; left: 350px; top: 152px;
    font: 400 17px/24px "Cinzel", serif; color: var(--ink);
  }
  .front-photo {
    position: absolute; left: 0; top: 386px; width: 515px; height: 386px;
    background:
      radial-gradient(ellipse at 35% 70%, var(--photo-front-b) 0%, rgba(217,207,195,0) 55%),
      linear-gradient(90deg, var(--photo-front-a) 0%, #8c8077 30%, #e8e2dc 60%, var(--photo-front-c) 85%, #ffffff 100%);
  }
</style>
</head>
<body>
<div class="canvas">
  <span class="page-number">3</span>

  <div class="trim-line trim-line--left"></div>
  <div class="trim-line trim-line--right"></div>

  <section class="back-cover">
    <h2 class="back-title">
      <span class="back-title__line">HANDS</span>
      <span class="back-title__line">THAT</span>
      <span class="back-title__line">STAY</span>
    </h2>
    <p class="back-subtitle">SELECTING A<br>TRUSTED ELDER<br>SUPPORT SERVICE</p>
    <div class="back-copy">
      <p>Lorem ipsum dolor sit amet consectetuer hutyu adipiscing elit. Aenean commodo ligula eget no dolor. Aenean massa. Cum sociis natoque nulla penatibus et magnis dis parturient montes, nascetur ridiculus mus. Donec quam felis, ultricies loput nec, pellentesque eu, pretium quis, sem. Nulla consequat massa quis enim. Donec pede justo,</p>
      <p>In enim justo, rhoncus ut, imperdiet a, venenatis vitae, justo. Nullam dictum felis eu pede mollis pretium. Integer tincidunt. Cras dapibus. Vivamus elementum semper nisi. Aenean vulputate eleifend tellus. Aenean leo ligula, porttitor eu, consequat vitae,</p>
    </div>
    <div class="back-photo" role="img" aria-label="Photo of a nurse in blue scrubs standing beside a smiling senior man using a walker in a bright clinic hallway"></div>
  </section>

  <section class="spine">
    <div class="spine-text">
      <span class="spine-title">HANDS THAT STAY</span>
      <span class="spine-subtitle">SELECTING A TRUSTED ELDER SUPPORT SERVICE</span>
    </div>
  </section>

  <section class="front-cover">
    <h1 class="front-title">
      <span class="front-title__line">HANDS</span>
      <span class="front-title__line">THAT</span>
      <span class="front-title__line">STAY</span>
    </h1>
    <p class="front-subtitle">SELECTING A<br>TRUSTED ELDER<br>SUPPORT SERVICE</p>
    <div class="front-photo" role="img" aria-label="Photo of a young caregiver resting her hands on the shoulders of a smiling elderly woman by a bright window"></div>
  </section>
</div>
</body>
</html>
```